Copper Kite Pastimes- Retailer

Need to describe what Copper Kite Pastimes is, what products we carry with photos and descriptions, as well as pricing for each. shopping cart, purchase items by way of Zellpay and CoinDrift

Industry/Entity Type

Hobby / Entertainment

Coding

Coded - Design and coding required

Number of Pages Required

5+ page

Font styles to use
Sans Serif

Colors
0054AA
0677BA
7BADD7
CADEEF
E8F1F8
F0912C
F2A743
F7CA91
FBE8D2
FDF5EE
EE7325
F08F49
F5BC92
FAE3D3
FDF4ED

Requirements
Must have
• Product pages, shopping cart, checkout
Nice to have
• Video/gif, of working train or slot car tracks
Should not have
• Cartoon characters or images

```html
<!DOCTYPE html>
<html lang="en">
<head>
<meta charset="utf-8">
<title>Checkout · Copper Kite Pastimes</title>
<link href="https://fonts.googleapis.com/css2?family=Inter:ital,wght@0,400;0,500;0,600;0,700;1,400&display=swap" rel="stylesheet">
<style>
  :root {
    --bg: #0e1a2e;
    --bar: #081221;
    --card: #12213a;
    --card-border: #1d3152;
    --field: #0a1424;
    --field-border: #22375a;
    --text: #ffffff;
    --soft: #cadeef;
    --muted: #7badd7;
    --blue: #0677ba;
    --blue-bright: #2f7fd6;
    --orange: #f2a743;
    --orange-deep: #f0912c;
    --button: #2b3a4f;
    --rule: #1f3150;
  }
  * { box-sizing: border-box; margin: 0; padding: 0; }
  html, body { width: 1200px; height: 1138px; overflow: hidden; }
  body { background: var(--bg); color: var(--text); font-family: "Inter", sans-serif; position: relative; }

  .site-header { height: 56px; background: var(--bar); border-bottom: 1px solid var(--rule); display: flex; align-items: center; justify-content: space-between; padding: 0 73px 0 75px; }
  .brand { display: flex; align-items: center; gap: 9px; font-weight: 700; font-size: 14px; letter-spacing: .04em; color: var(--text); }
  .brand-dot { width: 22px; height: 22px; border-radius: 50%; background: var(--orange-deep); }
  .main-nav { display: flex; align-items: center; gap: 18px; }
  .main-nav a { color: var(--muted); text-decoration: none; font-size: 13px; font-weight: 600; letter-spacing: .06em; }
  .cart-button { display: flex; align-items: center; gap: 7px; height: 30px; padding: 0 14px; background: var(--blue-bright); border-radius: 5px; color: #fff !important; letter-spacing: 0 !important; font-size: 14px !important; font-weight: 700 !important; }
  .cart-count { width: 15px; height: 15px; border-radius: 50%; background: var(--orange); color: #081221; font-size: 9px; display: flex; align-items: center; justify-content: center; }

  .checkout { width: 598px; margin: 0 auto; padding-top: 54px; }
  .checkout h1 { font-size: 29px; font-weight: 700; letter-spacing: -.02em; line-height: 34px; }
  .lede { color: var(--muted); font-size: 14.5px; margin-top: 4px; }

  .panel { background: var(--card); border: 1px solid var(--card-border); border-radius: 9px; padding: 19px 20px 20px; margin-top: 15px; }
  .panel:first-of-type { margin-top: 25px; }
  .panel h2 { font-size: 14.5px; font-weight: 700; letter-spacing: -.02em; line-height: 18px; margin-bottom: 11px; }

  .field-row { display: grid; grid-template-columns: 1fr 1fr; gap: 12px; }
  .field { margin-bottom: 12px; }
  .field-row .field { margin-bottom: 12px; }
  .panel > .field-row:last-child .field { margin-bottom: 0; }
  .field label { display: block; font-size: 10px; font-weight: 600; color: var(--muted); letter-spacing: .05em; line-height: 12px; margin-bottom: 4px; }
  .field .input { height: 32px; background: var(--field); border: 1px solid var(--field-border); border-radius: 5px; padding: 0 11px; display: flex; align-items: center; font-size: 12px; font-weight: 500; color: var(--text); }

  .pay-options { display: grid; grid-template-columns: 1fr 1fr; gap: 12px; }
  .pay-option { height: 105px; background: var(--field); border: 2px solid var(--field-border); border-radius: 8px; padding: 20px 17px 0; }
  .pay-icon { width: 26px; height: 26px; border-radius: 50%; background: var(--blue-bright); margin-bottom: 8px; }
  .pay-name { font-size: 14.5px; font-weight: 700; letter-spacing: -.02em; }
  .pay-handle { font-size: 11px; color: var(--muted); margin-top: 3px; }

  .summary-line { display: flex; justify-content: space-between; font-size: 12.5px; padding-bottom: 8px; border-bottom: 1px solid var(--rule); }
  .summary-line span:first-child { color: var(--muted); }
  .summary-line span:last-child { font-weight: 700; }
  .summary-total { display: flex; justify-content: space-between; align-items: center; padding-top: 9px; }
  .summary-total span:first-child { font-size: 16px; font-weight: 700; letter-spacing: -.02em; }
  .summary-total span:last-child { font-size: 20px; font-weight: 700; color: var(--orange); }

  .continue { width: 100%; height: 42px; margin-top: 15px; border: none; border-radius: 5px; background: var(--button); color: var(--text); font: 700 14px "Inter", sans-serif; letter-spacing: -.02em; }

  .site-footer { position: absolute; top: 928px; left: 0; width: 1200px; height: 210px; background: var(--bar); border-top: 1px solid var(--rule); }
  .footer-cols { display: grid; grid-template-columns: 247px 248px 248px 1fr; padding: 35px 117px 0; height: 162px; }
  .footer-cols h3 { font-size: 13px; font-weight: 700; margin-bottom: 8px; }
  .footer-cols ul { list-style: none; }
  .footer-cols li { font-size: 12px; color: var(--muted); line-height: 19.5px; display: flex; align-items: center; gap: 7px; }
  .footer-brand .brand { font-size: 12.5px; margin-top: 2px; }
  .footer-brand .brand-dot { width: 20px; height: 20px; }
  .tagline { font-size: 11px; font-style: italic; color: var(--muted); margin-top: 15px; }
  .footer-base { margin: 0 117px; border-top: 1px solid var(--rule); display: flex; justify-content: space-between; padding-top: 12px; font-size: 11px; color: var(--muted); }
  .footer-base span:first-child { color: var(--soft); }
  .icon { width: 11px; height: 11px; flex: none; }
</style>
</head>
<body>
  <header class="site-header">
    <div class="brand"><span class="brand-dot"></span>COPPER KITE PASTIMES</div>
    <nav class="main-nav">
      <a href="#">HOME</a>
      <a href="#">SHOP</a>
      <a href="#">ABOUT</a>
      <a href="#">CONTACT</a>
      <a href="#" class="cart-button">
        <svg class="icon" style="width:15px;height:15px" viewBox="0 0 24 24" fill="none" stroke="#fff" stroke-width="2"><path d="M6 3h12l2 5v12a1 1 0 0 1-1 1H5a1 1 0 0 1-1-1V8z"/><path d="M4 8h16M9 12a3 3 0 0 0 6 0"/></svg>
        <span class="cart-count">1</span>Cart
      </a>
    </nav>
  </header>

  <main class="checkout">
    <h1>Checkout</h1>
    <p class="lede">Fill in your details and choose how to pay</p>

    <section class="panel">
      <h2>Your Information</h2>
      <div class="field"><label>FULL NAME *</label><div class="input">vcvvc</div></div>
      <div class="field-row">
        <div class="field"><label>EMAIL *</label><div class="input">vvcv</div></div>
        <div class="field"><label>PHONE</label><div class="input">vvvcc</div></div>
      </div>
      <div class="field"><label>STREET ADDRESS</label><div class="input">ccc</div></div>
      <div class="field-row">
        <div class="field"><label>CITY</label><div class="input">cc</div></div>
        <div class="field"><label>ZIP CODE</label><div class="input">ccc</div></div>
      </div>
    </section>

    <section class="panel">
      <h2>Payment Method</h2>
      <div class="pay-options">
        <div class="pay-option"><div class="pay-icon"></div><div class="pay-name">Zellpay</div><div class="pay-handle">@CopperKitePastimes</div></div>
        <div class="pay-option"><div class="pay-icon"></div><div class="pay-name">CoinDrift</div><div class="pay-handle">coindrift.me/CopperKite</div></div>
      </div>
    </section>

    <section class="panel">
      <h2>Order Summary</h2>
      <div class="summary-line"><span>Classic Racing Slot Car Set × 1</span><span>$59.95</span></div>
      <div class="summary-total"><span>Total</span><span>$59.95</span></div>
    </section>

    <button class="continue">Select a Payment Method to Continue</button>
  </main>

  <footer class="site-footer">
    <div class="footer-cols">
      <div class="footer-brand">
        <div class="brand"><span class="brand-dot"></span>COPPER KITE PASTIMES</div>
        <p class="tagline">"Hands On, Heads Up. Built To Be Played."</p>
      </div>
      <div>
        <h3>Shop</h3>
        <ul><li>Die-Cast Trucks</li><li>Model Trains</li><li>Slot Cars</li><li>Accessories</li></ul>
      </div>
      <div>
        <h3>Company</h3>
        <ul><li>About Us</li><li>Contact</li><li>Cart</li></ul>
      </div>
      <div>
        <h3>Get In Touch</h3>
        <ul>
          <li><svg class="icon" viewBox="0 0 24 24" fill="#e5483b"><path d="M6.6 10.8a15 15 0 0 0 6.6 6.6l2.2-2.2a1 1 0 0 1 1-.25 11.4 11.4 0 0 0 3.6.6 1 1 0 0 1 1 1V20a1 1 0 0 1-1 1A17 17 0 0 1 3 4a1 1 0 0 1 1-1h3.5a1 1 0 0 1 1 1c0 1.25.2 2.450.6 3.6a1 1 0 0 1-.25 1z"/></svg>555-014-2291</li>
          <li><svg class="icon" viewBox="0 0 24 24" fill="#e8f1f8"><rect x="2" y="5" width="20" height="14" rx="1"/></svg>dale@copperkitepastimes.example</li>
          <li><svg class="icon" viewBox="0 0 24 24" fill="none" stroke="#4fb3f0" stroke-width="2"><circle cx="12" cy="12" r="9"/><path d="M3 12h18M12 3c3 3 3 15 0 18M12 3c-3 3-3 15 0 18"/></svg>www.copperkitepastimes.example</li>
        </ul>
      </div>
    </div>
    <div class="footer-base">
      <span>© 2025 Copper Kite Pastimes · Dale Rourke</span>
      <span>Made for collectors &amp; hobbyists everywhere</span>
    </div>
  </footer>
</body>
</html>
```